Business Card Design

our business is purchasing, rehabbing and flipping homes. Design a house in the palm of a hand. This card is for a new company based in Georgia. So we buy homes that have been foreclosed, short sales,abandond, old homes and vacant homes.
We help improve the communities that we work in. We would like to see designs that use a black background with green accent and other colors that blend and don't take away from the logo and other important information.

Industry/Entity Type

Business

Contact Information for Business Card

Mavenbrook Holdings
Turning Old Doors Into New Starts
2738 Fenwick Lane
Duluth GA 30418
Office: 678-555-0192
mavenbrookholdingsllc.example

```html
<!DOCTYPE html>
<html lang="en">
<head>
<meta charset="utf-8">
<title>Mavenbrook Holdings – Business Card</title>
<link rel="stylesheet" href="https://fonts.googleapis.com/css2?family=Alegreya:wght@500&family=Crimson+Text:wght@400;600&display=swap">
<style>
  :root {
    --page-bg: #d8d3cb;
    --card-black: #111111;
    --brand-green: #5fae3f;
    --panel-green: #5aa83d;
    --panel-white: #f4f4f4;
    --ink: #111111;
    --soft-white: #e8e8e8;
    --icon-bg: #d6d6d6;
  }
  * { margin: 0; padding: 0; box-sizing: border-box; }
  html, body {
    width: 1200px;
    height: 892px;
    overflow: hidden;
    background: var(--page-bg);
  }
  .canvas {
    position: relative;
    width: 1200px;
    height: 892px;
  }
  .card {
    position: absolute;
    left: 100px;
    top: 160px;
    width: 1000px;
    height: 571px;
    background: var(--card-black);
    overflow: hidden;
    box-shadow: 0 12px 30px rgba(0,0,0,0.25);
  }
  .card-panels {
    position: absolute;
    inset: 0;
    width: 1000px;
    height: 571px;
  }
  .brand {
    position: absolute;
    left: 270px;
    top: 118px;
  }
  .brand-name {
    font-family: "Alegreya", serif;
    font-weight: 500;
    font-size: 58px;
    line-height: 1;
    color: var(--brand-green);
    white-space: nowrap;
  }
  .brand-tagline {
    margin-top: 6px;
    margin-left: 22px;
    font-family: "Crimson Text", serif;
    font-size: 17px;
    letter-spacing: 3px;
    color: var(--soft-white);
    white-space: nowrap;
  }
  .services {
    position: absolute;
    right: 50px;
    top: 310px;
    text-align: right;
    font-family: "Crimson Text", serif;
    color: var(--ink);
  }
  .services-title {
    font-size: 32px;
    font-weight: 600;
    line-height: 1.05;
  }
  .services-item {
    font-size: 21px;
    line-height: 1.3;
  }
  .person {
    position: absolute;
    left: 40px;
    top: 296px;
    font-family: "Crimson Text", serif;
    color: var(--ink);
  }
  .person-name {
    font-size: 54px;
    font-weight: 600;
    line-height: 1;
  }
  .person-role {
    font-size: 18px;
    margin-left: 22px;
    margin-top: 2px;
  }
  .contact-list {
    position: absolute;
    left: 56px;
    top: 404px;
    list-style: none;
    font-family: "Crimson Text", serif;
    font-size: 23px;
    color: var(--ink);
  }
  .contact-item {
    display: flex;
    align-items: center;
    height: 46px;
  }
  .contact-icon {
    width: 24px;
    height: 24px;
    margin-right: 20px;
    flex: none;
  }
</style>
</head>
<body>
<div class="canvas">
  <article class="card">
    <svg class="card-panels" viewBox="0 0 1000 571" aria-hidden="true">
      <polygon class="panel-white" points="500,263 1000,263 1000,525 720,520" fill="var(--panel-white)"/>
      <polygon class="panel-green" points="0,274 470,274 690,485 710,555 0,555" fill="var(--panel-green)"/>
    </svg>

    <header class="brand">
      <div class="brand-name">Mavenbrook Holdings</div>
      <div class="brand-tagline">Turning Old Doors Into New Starts</div>
    </header>

    <section class="services">
      <div class="services-title">Service</div>
      <div class="services-item">purchasing</div>
      <div class="services-item">rehabbing and flipping homes</div>
    </section>

    <section class="person">
      <div class="person-name">Employee name</div>
      <div class="person-role">Managing Director</div>
    </section>

    <ul class="contact-list">
      <li class="contact-item">
        <svg class="contact-icon" viewBox="0 0 24 24" aria-hidden="true">
          <rect width="24" height="24" rx="3" fill="var(--icon-bg)"/>
          <path d="M8 6c1 0 2 2 2 3s-1 1-1 2 2 3 3 3 1-1 2-1 3 1 3 2-1 2-2 2c-4 0-9-5-9-9 0-1 1-2 2-2z" fill="var(--ink)"/>
        </svg>
        <span>678-555-0192</span>
      </li>
      <li class="contact-item">
        <svg class="contact-icon" viewBox="0 0 24 24" aria-hidden="true">
          <rect width="24" height="24" rx="3" fill="var(--icon-bg)"/>
          <circle cx="12" cy="12" r="6" fill="none" stroke="var(--ink)" stroke-width="1.6"/>
          <ellipse cx="12" cy="12" rx="2.5" ry="6" fill="none" stroke="var(--ink)" stroke-width="1.2"/>
          <line x1="6" y1="12" x2="18" y2="12" stroke="var(--ink)" stroke-width="1.2"/>
        </svg>
        <span>www.mavenbrookholdingsllc.example</span>
      </li>
      <li class="contact-item">
        <svg class="contact-icon" viewBox="0 0 24 24" aria-hidden="true">
          <rect width="24" height="24" rx="3" fill="var(--icon-bg)"/>
          <path d="M12 5a5 5 0 0 1 5 5c0 4-5 9-5 9s-5-5-5-9a5 5 0 0 1 5-5z" fill="var(--ink)"/>
          <circle cx="12" cy="10" r="1.8" fill="var(--icon-bg)"/>
        </svg>
        <span>2738 Fenwick Lane Duluth GA 30418</span>
      </li>
    </ul>
  </article>
</div>
</body>
</html>
```